Solvane Travel Planners needs an bold logo and business card design

Thanks you all for helping me with this project your assistance is appriciated
I am starting a home based travel agency and I need a bold and eye catching logo and business card designed.
I want to convey a sense of FREEDOM, expertise, customer service for travel customers
Solvane travel planners is a full service travel agency focused on customer service and adding value to a vacation and travel planning.
my idea is for a card that looks like an cruise ship boarding pass or passport with stamps with a back drop of beautiful beach scene, resort hotel and happiness.
The logo should be eye catching, unique but give a sense of freedom and it should be travel related
We want to give customers a sense of Freedom from travel planning, freedom from researching cruises and hotels and freedom to enjoy a wonderful cost effective vacation.

Target Market(s)

Customers considering travel for vacations, family reunions, business and weddings

Industry/Entity Type

Travel Industry

Contact Information for Business Card

Solvane Travel Planners
Marcus Helbrook Owner
MHelbrook@SolvaneTravelPlanners.com
SolvaneTravelPlanners.com
(555) 214-7830

Logo Text

“One’s destination is never a place, but a new way of seeing things.”

Font styles to use
Serif

Colors
85cae6
0492cd
ec1f27
e667a6
b768aa
33b8a4

Requirements
Must have
• The Logo you create should be on the busoness card
• should be clean, easy to read and attractive
• something you that would make you want to work with a travel agent
Nice to have
• should have cruise ship, hotel on the card or something that conveys travel
Should not have
• Should not have the american flag
• no yellow on the card

```html
<!DOCTYPE html>
<html lang="en">
<head>
<meta charset="utf-8">
<title>Solvane Travel Planners – Business Card</title>
<link rel="stylesheet" href="https://fonts.googleapis.com/css2?family=Tinos:wght@400;700&display=swap">
<style>
  :root {
    --page-bg: #e9e7e3;
    --card-white: #ffffff;
    --ink: #1a1a1a;
    --band-black: #0d0d0d;
    --teal: #2cb9a6;
    --smudge-dark: #2a2a2a;
    --smudge-light: #8a8a8a;
    --icon-line: #222222;
  }
  * { box-sizing: border-box; margin: 0; padding: 0; }
  html, body {
    width: 1200px; height: 1200px; overflow: hidden;
    background: var(--page-bg);
    font-family: "Tinos", "Times New Roman", serif;
    color: var(--ink);
  }
  .sheet {
    position: relative; width: 1200px; height: 1200px;
    display: flex; flex-direction: column; align-items: center; justify-content: center; gap: 58px;
  }
  .card {
    position: relative; width: 880px; height: 503px;
    background: var(--card-white);
    box-shadow: 0 6px 18px rgba(0,0,0,.18);
    overflow: hidden;
  }

  /* Front */
  .front .brand {
    position: absolute; left: 0; right: 0; top: 150px;
    display: flex; align-items: center; justify-content: center; gap: 16px;
  }
  .brand-dot {
    width: 34px; height: 34px; border-radius: 50%; background: var(--teal);
  }
  .brand-name {
    font-weight: 700; color: var(--teal); font-size: 44px; letter-spacing: 1px;
  }
  .front .web-band {
    position: absolute; left: 0; right: 0; top: 330px; height: 80px;
    background: var(--band-black);
    display: flex; align-items: center; justify-content: center;
    color: var(--card-white); font-size: 30px; letter-spacing: .5px;
  }

  /* Back */
  .back .dark-panel {
    position: absolute; left: 0; top: 0; bottom: 0; width: 390px;
    background: var(--band-black);
  }
  .back .smudge {
    position: absolute; left: 170px; top: 0; bottom: 0; width: 220px;
    background: linear-gradient(90deg, var(--band-black) 0%, var(--smudge-dark) 35%, var(--smudge-light) 60%, #5a5a5a 100%);
  }
  .back .edge-slot {
    position: absolute; left: -14px; top: 40px; width: 36px; height: 330px;
    border-radius: 18px; background: var(--card-white);
  }
  .back .brand {
    position: absolute; left: 50px; top: 150px; width: 330px;
    display: flex; align-items: center; gap: 12px;
  }
  .back .brand-dot { width: 26px; height: 26px; flex: none; }
  .back .brand-name { font-size: 30px; line-height: 1.15; }

  .contact-list {
    position: absolute; left: 440px; top: 60px; right: 30px;
    list-style: none;
  }
  .contact-item {
    display: flex; align-items: center; gap: 16px; margin-bottom: 52px;
    font-size: 21px;
  }
  .contact-item.person { font-size: 27px; margin-bottom: 60px; }
  .contact-item svg { width: 34px; height: 34px; flex: none; }
</style>
</head>
<body>
<main class="sheet">

  <section class="card front" aria-label="Business card front">
    <div class="brand">
      <span class="brand-dot"></span>
      <span class="brand-name">Solvane Travel Planners</span>
    </div>
    <div class="web-band">SolvaneTravelPlanners.com</div>
  </section>

  <section class="card back" aria-label="Business card back">
    <div class="dark-panel"></div>
    <div class="smudge" role="img" aria-label="Textured grey brush-stroke decoration"></div>
    <div class="edge-slot"></div>
    <div class="brand">
      <span class="brand-dot"></span>
      <span class="brand-name">Solvane Travel Planners</span>
    </div>

    <ul class="contact-list">
      <li class="contact-item person">
        <svg viewBox="0 0 34 34" aria-hidden="true">
          <rect x="2" y="2" width="30" height="30" rx="6" fill="none" stroke="var(--icon-line)" stroke-width="2.5"/>
          <circle cx="17" cy="13" r="5" fill="var(--icon-line)"/>
          <path d="M8 27c1-6 5-8 9-8s8 2 9 8z" fill="var(--icon-line)"/>
        </svg>
        <span>Marcus Helbrook Owner</span>
      </li>
      <li class="contact-item">
        <svg viewBox="0 0 34 34" aria-hidden="true">
          <rect x="2" y="2" width="30" height="30" rx="6" fill="none" stroke="var(--icon-line)" stroke-width="2.5"/>
          <path d="M11 8h4l2 6-3 2c1 3 3 5 6 6l2-3 6 2v4c-10 1-18-7-17-17z" fill="var(--icon-line)"/>
        </svg>
        <span>(555) 214-7830</span>
      </li>
      <li class="contact-item">
        <svg viewBox="0 0 34 34" aria-hidden="true">
          <rect x="2" y="2" width="30" height="30" rx="6" fill="none" stroke="var(--icon-line)" stroke-width="2.5"/>
          <rect x="8" y="11" width="18" height="12" fill="none" stroke="var(--icon-line)" stroke-width="2"/>
          <path d="M8 11l9 7 9-7" fill="none" stroke="var(--icon-line)" stroke-width="2"/>
        </svg>
        <span>MHelbrook@SolvaneTravelPlanners.com</span>
      </li>
      <li class="contact-item">
        <svg viewBox="0 0 34 34" aria-hidden="true">
          <rect x="2" y="2" width="30" height="30" rx="6" fill="none" stroke="var(--icon-line)" stroke-width="2.5"/>
          <circle cx="17" cy="17" r="9" fill="none" stroke="var(--icon-line)" stroke-width="2"/>
          <path d="M8 17h18M17 8c-4 5-4 13 0 18M17 8c4 5 4 13 0 18" fill="none" stroke="var(--icon-line)" stroke-width="1.6"/>
        </svg>
        <span>SolvaneTravelPlanners.com</span>
      </li>
    </ul>
  </section>

</main>
</body>
</html>
```